(Wordpress)Website Design - No requirements! Sign Your name at the bottom of the site!

Dear Designer,

I am looking for a designer who is interested in a long-term business realtionship.
I already have 2 more designs to get done IMMEDIATELY after this website..
1.) An email brochure matching the website theme.
2.) A Billboard. BOTH MATCHING THE WEBSITE THEME

For this project, a bonus WILL be given.

Go to vaultnest.com as Site Inspiration

Please take this opportunity to design an existing wordpress website, FUNDSWIFTLANE.com, in whatever form your creativity takes you

I have no requirements other than a CREATIVE and OUT-OF -THE-BOX Design. Something Pretty and Eye Catching; a website that someone logs onto and doesnt want to leave

I have purchased a theme called velorant. You dont need to use it...But Info can be found at

http://skinbazaar.example/item/velorant-premium-wordpress-theme/full_screen_preview/482715

I have attached my logos and a PDF with a short story about what our company does.

Thank You,
-Tobin
PS I HAVE ANOTHER 2 DESIGNS TO DO AFTER THIS PROJECT.
also, IF YOU KNOW OF SOMEONE WHO DOES SEO WORK, I AM LOOKING FOR A FULL-TIME EMPLOYEE

Target Market(s)

Business Owners in a state of finacial NEED

Industry/Entity Type

Business

Requirements
Must have
• COLORFUL, EYE CATCHING

```html
<!DOCTYPE html>
<html lang="en">
<head>
<meta charset="utf-8">
<title>FundSwiftLane</title>
<link rel="stylesheet" href="https://fonts.googleapis.com/css2?family=Cabin:ital,wght@0,400;0,500;0,600;1,400&family=Yanone+Kaffeesatz:wght@400;500&family=Arimo&display=swap">
<style>
:root{
  --ink:#555;
  --ink-dark:#333;
  --blue:#2f4fa8;
  --link-blue:#3a4fa8;
  --green:#6f9a22;
  --green-bright:#9ccc1c;
  --panel:#f1f1f1;
  --line:#d6d6d6;
  --footer:#333;
  --sky:#4aa6e4;
}
*{box-sizing:border-box;margin:0;padding:0}
html,body{width:1145px;height:1200px;overflow:hidden;background:#fff}
body{font-family:"Cabin",sans-serif;color:var(--ink)}
.page{position:absolute;left:0;top:0;width:1050px;height:1100px;transform:scale(1.0905);transform-origin:0 0}
.abs{position:absolute}

/* header */
.logo{left:48px;top:24px;display:flex;align-items:center;gap:8px}
.logo-dot{width:40px;height:40px;border-radius:50%;background:var(--green)}
.logo-name{font-size:34px;font-weight:500;color:var(--blue);letter-spacing:-.5px}
.search{left:872px;top:34px;width:130px;height:24px;border:1px solid #ccc;border-radius:2px;box-shadow:inset 0 1px 2px rgba(0,0,0,.1);font-size:11px;font-style:italic;color:#999;padding:5px 8px;background:#fff}
.search svg{position:absolute;right:6px;top:6px}

/* nav */
.nav{left:45px;top:89px;width:960px;height:49px;background:linear-gradient(#fafafa,#ececec);border-radius:3px 3px 0 0;display:flex}
.nav a{font-size:13.5px;color:#444;text-decoration:none;display:flex;align-items:center;justify-content:center;border-right:1px solid var(--line);height:100%}
.nav a.active{background:#dcdcdc;color:var(--blue)}
.cta{left:794px;top:93px;width:206px;height:43px;border-radius:4px;background:linear-gradient(#b4dd3c,var(--green-bright) 50%,#86b314);border:1px solid #7ea51a;display:flex;align-items:center;padding-left:26px;gap:12px;font-family:"Yanone Kaffeesatz",sans-serif;font-size:23px;color:#3a4a10}
.cta-icon{width:18px;height:18px;border-radius:50%;background:#333;display:flex;align-items:center;justify-content:center}

/* hero */
.hero{left:0;top:138px;width:1050px;height:300px;background:linear-gradient(#f6f6f6,#e9e9e9);border-top:2px solid #fff;border-bottom:2px solid #fff;box-shadow:0 -1px 0 #ddd,0 1px 0 #ddd}
.hero-art{left:130px;top:12px;width:250px;height:282px;background:radial-gradient(circle at 45% 50%,#b9bec9,#dcdde0 70%,#ececec)}
.hero-quote{left:411px;top:58px;width:540px;font-size:17.5px;line-height:30px;color:#555}
.hero-link{left:766px;top:130px;font-size:12.5px;color:var(--link-blue);display:flex;align-items:center;gap:8px}
.hero-dots{left:415px;top:200px}

/* charity strip */
.charity{left:45px;top:441px;width:960px;height:111px;background:linear-gradient(#f6f6f6,#ececec);border:1px solid #e3e3e3;border-radius:3px}
.charity-title{left:0;top:18px;width:182px;text-align:center;font-size:21px;line-height:32px;color:#666;font-weight:400}
.charity-divider{left:182px;top:0;width:1px;height:109px;background:var(--line)}
.charity-icon{left:208px;top:32px}
.charity-text{left:291px;top:20px;width:640px;font-size:12.5px;line-height:20px;color:#555}
.charity-contact{left:291px;top:70px;font-size:15px;color:var(--green);display:flex;gap:27px}

/* news */
.news{left:45px;top:571px;width:252px;height:281px;background:linear-gradient(#f4f4f4,#ececec);border-radius:3px;box-shadow:0 1px 2px rgba(0,0,0,.15);padding:12px 10px 0 11px}
.news h3{font-size:17px;font-weight:400;color:var(--blue);padding-bottom:12px;border-bottom:1px solid #ccc;width:226px}
.news-item{font-family:"Arimo",sans-serif;padding:14px 0 8px 13px;border-bottom:1px dotted #555;width:231px;position:relative}
.news-item+.news-item{border-bottom:none}
.news-item::before{content:"";position:absolute;left:1px;top:19px;border-left:5px solid #777;border-top:3.5px solid transparent;border-bottom:3.5px solid transparent}
.news-title{font-size:12.5px;line-height:16px;color:#111}
.news-body{font-size:11px;line-height:13px;color:#333;margin-top:5px}
.news-meta{font-size:10px;color:#111;margin-top:8px}
.news-meta a{color:var(--blue);text-decoration:none}

/* newsletter */
.signup{left:45px;top:865px;width:252px;height:131px;background:linear-gradient(#6cc0f0,var(--sky) 55%,#3d95d8);border-radius:3px;box-shadow:0 1px 2px rgba(0,0,0,.2)}
.signup-title{left:47px;top:15px;font-size:17px;color:#fff}
.signup-icon{left:10px;top:17px}
.signup-input{left:24px;top:53px;width:200px;height:28px;background:#fff;border:1px solid #aaa;font-size:11px;font-style:italic;color:#999;padding:7px 8px}
.btn{background:linear-gradient(#555,#222);color:#fff;font-size:10.5px;font-style:italic;border-radius:2px;display:flex;align-items:center;justify-content:center;box-shadow:0 1px 2px rgba(0,0,0,.4)}
.signup .btn{left:163px;top:95px;width:60px;height:24px}

/* welcome */
.welcome-title{left:321px;top:580px;font-size:23px;color:var(--green);font-weight:400}
.welcome-text{left:321px;top:631px;width:677px;font-size:11px;line-height:20px;text-align:justify;color:#444}

/* quote form */
.quote{left:321px;top:784px;width:676px;height:191px;background:linear-gradient(#f2f2f2,#fafafa 90%,#fff);border-radius:4px}
.quote h3{position:absolute;left:20px;top:15px;font-size:17px;font-weight:400;color:var(--green)}
.field-label{font-size:11px;color:#444;text-align:right;line-height:13px}
.field{width:160px;height:29px;background:#fff;border:1px solid #c9c9c9;border-radius:2px;box-shadow:inset 0 1px 2px rgba(0,0,0,.08)}
.select{font-size:11px;font-style:italic;color:#666;padding:8px 10px}
.select::after{content:"";position:absolute;right:10px;top:12px;border-top:6px solid #444;border-left:6px solid transparent;border-right:6px solid transparent}
.quote .btn{left:587px;top:165px;width:60px;height:24px}

/* footer */
.footer{left:0;top:1017px;width:1050px;height:83px;background:var(--footer)}
.footer-nav{left:46px;top:19px;font-size:12.5px;color:#eee;display:flex;gap:10px}
.footer-nav span.sep{color:#999}
.copyright{left:46px;top:47px;font-size:12.5px;color:#ddd;word-spacing:1px}
.social{top:28px;width:27px;height:27px;border-radius:50%;background:#fff}
</style>
</head>
<body>
<div class="page">

  <header>
    <div class="abs logo"><span class="logo-dot"></span><span class="logo-name">FundSwiftLane</span></div>
    <div class="abs search">Search
      <svg width="11" height="11" viewBox="0 0 11 11"><circle cx="4.5" cy="4.5" r="3.3" fill="none" stroke="#aaa" stroke-width="1.4"/><line x1="7" y1="7" x2="10" y2="10" stroke="#aaa" stroke-width="1.6"/></svg>
    </div>
    <nav class="abs nav">
      <a class="active" style="width:96px">Home</a>
      <a style="width:108px">About Us</a>
      <a style="width:98px">Careers</a>
      <a style="width:147px">Free Downloads</a>
      <a style="width:161px">SwiftLane Charity</a>
      <a style="width:116px;border-right:none">Contact Us</a>
    </nav>
    <div class="abs cta"><span class="cta-icon"><svg width="8" height="8" viewBox="0 0 8 8"><path d="M1 1 L6 4 L1 7Z" fill="#b4dd3c"/></svg></span>GET STARTED NOW!</div>
  </header>

  <section class="abs hero">
    <div class="abs hero-art" role="img" aria-label="Businessman in a suit standing in a sketched circle, drawing a globe beside him"></div>
    <p class="abs hero-quote">They even have a network of business coaches and consultants which offered me true, sound business advice!</p>
    <div class="abs hero-link">Click here for Learn more
      <svg width="12" height="9" viewBox="0 0 12 9"><path d="M0 0 L6 4.5 L0 9Z M6 0 L12 4.5 L6 9Z" fill="var(--link-blue)"/></svg>
    </div>
    <svg class="abs hero-dots" width="510" height="14" viewBox="0 0 510 14">
      <line x1="0" y1="7" x2="180" y2="7" stroke="#888" stroke-width="1"/>
      <line x1="330" y1="7" x2="510" y2="7" stroke="#888" stroke-width="1"/>
      <circle cx="194" cy="7" r="4.5" fill="#555"/>
      <circle cx="225" cy="7" r="4.5" fill="#3a5ab8"/>
      <circle cx="256" cy="7" r="4.5" fill="#555"/>
      <circle cx="287" cy="7" r="4.5" fill="#555"/>
      <circle cx="318" cy="7" r="4.5" fill="#555"/>
    </svg>
  </section>

  <section class="abs charity">
    <h2 class="abs charity-title">SwiftLane<br>Charity</h2>
    <div class="abs charity-divider"></div>
    <svg class="abs charity-icon" width="56" height="54" viewBox="0 0 56 54">
      <ellipse cx="26" cy="24" rx="25" ry="21" fill="#fff" stroke="#c8c8c8"/>
      <path d="M12 40 L8 52 L22 43Z" fill="#fff" stroke="#c8c8c8"/>
      <circle cx="27" cy="24" r="15" fill="#2f6fc0"/>
      <path d="M20 17 Q19 22 25 29 Q31 34 35 32 L33 28 L30 29 Q27 27 25 24 L26 21 L22 17Z" fill="#fff"/>
    </svg>
    <p class="abs charity-text">At FundSwiftLane, we are committed to giving back. We founded this company on the basis of ethics and morale. From the moment we opened our business doors, we initiated SwiftLaneCharity</p>
    <div class="abs charity-contact"><span>Call us : 888-555-0142</span><span>E-mail : charity@fundswiftlane.com</span></div>
  </section>

  <aside class="abs news">
    <h3>Latest News</h3>
    <div class="news-item">
      <div class="news-title">Nam molestie pretium magna, nec facilisis nibh ultricies</div>
      <div class="news-body">Nulla quis lorem neque, mattis venenatis lectus. In interdum ullamcorper dolor ...</div>
      <div class="news-meta">by <a>John Doe</a> &nbsp;| &nbsp;29 Views</div>
    </div>
    <div class="news-item">
      <div class="news-title">Nam molestie pretium magna, nec facilisis nibh ultricies</div>
      <div class="news-body">Nulla quis lorem neque, mattis venenatis lectus. In interdum ullamcorper dolor ...</div>
      <div class="news-meta">by <a>John Doe</a> &nbsp;| &nbsp;29 Views</div>
    </div>
  </aside>

  <aside class="abs signup">
    <svg class="abs signup-icon" width="30" height="21" viewBox="0 0 30 21"><rect x="0.5" y="0.5" width="29" height="20" fill="#f4f8fb" stroke="#9ab"/><path d="M1 1 L15 12 L29 1" fill="none" stroke="#9ab"/></svg>
    <div class="abs signup-title">Sign up for News Letter</div>
    <div class="abs signup-input">Enter your mail ID</div>
    <div class="abs btn">SUBMIT</div>
  </aside>

  <main>
    <h1 class="abs welcome-title">Welcome to our site</h1>
    <p class="abs welcome-text">Sed ut perspiciatis unde omnis iste natus error sit voluptatem accusantium doloremque laudantium, totam rem aperiam, eaque ipsa quae ab illo inventore veritatis et quasi architecto beatae vitae dicta sunt explicabo. Nemo enim ipsam voluptatem quia voluptas sit aspernatur aut odit aut fugit, sed quia consequuntur magni dolores eos qui ratione voluptatem sequi nesciunt. Neque porro quisquam est, qui dolorem ipsum quia dolor sit amet, consectetur, adipisci velit, sed quia non numquam eius modi tempora incidunt ut labore et dolore magnam aliquam quaerat voluptatem. Ut enim ad minima veniam, quis nostrum exercitationem ullam corporis suscipit laboriosam, nisi ut aliquid ex ea commodi consequatu. Quis autem vel eum iure reprehenderit qui in ea voluptate velit esse quam nihil molestiae cons equatur, vel illum qui dolorem eum fugiat quo voluptas nulla pariatur.</p>

    <form class="abs quote">
      <h3>Get a Quote</h3>
      <div class="abs field-label" style="left:0;top:65px;width:102px">Company Name</div>
      <div class="abs field" style="left:115px;top:57px"></div>
      <div class="abs field-label" style="left:0;top:118px;width:102px">Name</div>
      <div class="abs field" style="left:115px;top:110px"></div>
      <div class="abs field-label" style="left:0;top:171px;width:102px">Phone</div>
      <div class="abs field" style="left:115px;top:163px"></div>

      <div class="abs field-label" style="left:290px;top:65px;width:103px">Email</div>
      <div class="abs field" style="left:406px;top:57px"></div>
      <div class="abs field-label" style="left:290px;top:118px;width:103px">Business Age</div>
      <div class="abs field select" style="left:406px;top:110px">Under 6 months</div>
      <div class="abs field-label" style="left:300px;top:168px;width:93px;text-align:left;padding-left:7px">Monthly Credit/<br>Debit Card Sales</div>
      <div class="abs field select" style="left:406px;top:163px">$0 - $2,500</div>
      <div class="abs btn">SUBMIT</div>
    </form>
  </main>

  <footer class="abs footer">
    <div class="abs footer-nav">
      <span>Home</span><span class="sep">|</span><span>Get Started Now</span><span class="sep">|</span><span>About Us</span><span class="sep">|</span><span>Careers</span><span class="sep">|</span><span>Free Downloads</span><span class="sep">|</span><span>SwiftLane Charity</span><span class="sep">|</span><span>Contact Us</span><span class="sep">|</span><span>Sitemap</span>
    </div>
    <div class="abs copyright">Copyright © 2012 www.fundswiftlane.com &nbsp;&nbsp; All rigths reserved</div>
    <div class="abs social" style="left:936px" role="img" aria-label="Social network link"></div>
    <div class="abs social" style="left:970px" role="img" aria-label="Social network link"></div>
  </footer>

</div>
</body>
</html>
```